Bar and Grill needs specials signage

I have attached a file called "daily specials" I need it changed - so there is 1 sign/poster for each day/special
also attached other items to show some styling. I want the new posters chalkboard format, styled along the lines of the drink designs attached.
The designs should be scaleable, and editable, I will print locally

```html
<!DOCTYPE html>
<html lang="en">
<head>
<meta charset="utf-8">
<title>Daily Specials – Saturday</title>
<link rel="stylesheet" href="https://fonts.googleapis.com/css2?family=Cabin+Sketch:wght@400;700&family=Kaushan+Script&family=Schoolbell&display=swap">
<style>
  :root {
    --board: #2f3530;
    --board-light: #5a605b;
    --chalk: #f4f4f0;
    --coral: #e4765c;
    --yellow: #e2a91e;
  }
  * { margin: 0; padding: 0; box-sizing: border-box; }
  html, body { width: 927px; height: 1200px; overflow: hidden; background: var(--board); }
  .poster {
    position: relative;
    width: 927px;
    height: 1200px;
    overflow: hidden;
    background:
      radial-gradient(ellipse 360px 260px at 50% 52%, rgba(140,146,140,0.45), transparent 70%),
      radial-gradient(ellipse 300px 220px at 45% 78%, rgba(120,126,120,0.35), transparent 70%),
      var(--board);
    color: var(--chalk);
  }
  .frame { position: absolute; inset: 0; }
  .heading {
    position: absolute; left: 0; right: 0; top: 78px;
    text-align: center;
    font-family: "Cabin Sketch", sans-serif;
    font-weight: 700;
    font-size: 76px;
    letter-spacing: 2px;
    line-height: 1;
  }
  .day {
    position: absolute; left: 0; right: 0; top: 148px;
    text-align: center;
    font-family: "Kaushan Script", cursive;
    font-size: 142px;
    line-height: 1.2;
  }
  .rule { position: absolute; height: 3px; background: var(--chalk); border-radius: 2px; }
  .rule--a { left: 178px; width: 596px; top: 353px; }
  .rule--b { left: 152px; width: 604px; top: 385px; }
  .rule--c { left: 152px; width: 622px; top: 651px; }
  .dish {
    position: absolute; left: 0; right: 0; top: 398px;
    text-align: center;
    font-family: "Cabin Sketch", sans-serif;
    font-weight: 700;
    color: var(--coral);
    line-height: 1;
  }
  .dish__method { font-size: 50px; letter-spacing: 2px; }
  .dish__name { font-size: 74px; margin-top: 14px; letter-spacing: 1px; }
  .dish__cut { font-size: 94px; margin-top: 2px; letter-spacing: 2px; }
  .dish-art {
    position: absolute; left: 168px; top: 680px; width: 572px; height: 228px;
    border-radius: 50%;
    background: radial-gradient(ellipse at 50% 50%, rgba(200,204,200,0.35), rgba(200,204,200,0.08) 65%, transparent 75%);
  }
  .accents { position: absolute; inset: 0; }
  .sides {
    position: absolute; left: 0; right: 0; top: 948px;
    text-align: center;
    font-family: "Schoolbell", cursive;
    font-size: 38px;
    line-height: 50px;
  }
</style>
</head>
<body>
<main class="poster">
  <svg class="frame" width="927" height="1200" viewBox="0 0 927 1200" aria-hidden="true">
    <rect x="44" y="32" width="839" height="1136" fill="none" stroke="var(--chalk)" stroke-width="4" rx="2"/>
    <rect x="52" y="40" width="823" height="1120" fill="none" stroke="var(--chalk)" stroke-width="1.5" opacity="0.5"/>
  </svg>

  <svg class="accents" width="927" height="1200" viewBox="0 0 927 1200" aria-hidden="true">
    <g stroke="var(--yellow)" stroke-width="3" stroke-linecap="round">
      <line x1="110" y1="180" x2="140" y2="192"/>
      <line x1="88" y1="258" x2="128" y2="258"/>
      <line x1="100" y1="330" x2="128" y2="326"/>
      <line x1="818" y1="180" x2="792" y2="192"/>
      <line x1="840" y1="258" x2="806" y2="258"/>
      <line x1="828" y1="330" x2="800" y2="326"/>
    </g>
    <g fill="none" stroke="var(--yellow)" stroke-width="3" stroke-linejoin="round">
      <path d="M90 836 L108 826 L140 890 L152 882 L156 922 L124 906 L134 898 Z"/>
      <path d="M822 678 L832 690 L788 752 L798 760 L760 774 L766 738 L776 744 Z"/>
    </g>
  </svg>

  <h1 class="heading">DAILY SPECIALS</h1>
  <p class="day">Saturday</p>
  <div class="rule rule--a"></div>
  <div class="rule rule--b"></div>

  <h2 class="dish">
    <span class="dish__method" style="display:block">“DUTCH OVEN”</span>
    <span class="dish__name" style="display:block">BONELESS BEEF</span>
    <span class="dish__cut" style="display:block">SHORT RIBS</span>
  </h2>
  <div class="rule rule--c"></div>

  <div class="dish-art" role="img" aria-label="Chalk sketch of three short ribs with a garlic bulb"></div>

  <p class="sides">Chipotle BBQ sauce &amp; crispy<br>onions, garlic, mashed potatoes,<br>fresh vegetables</p>
</main>
</body>
</html>
```